Web Design for Small Healthcare Startup

Hello,

We are seeking a Website Design for a healthcare company focusing on mobile vaccinations, employee health and wellness services onsite at businesses, and consulting services relating to Healthcare Entities in WA state. Our company’s mission is to “To aid in a healthier workplace”. Brightpath Rovers will provide on-site wellness services to employers that simplify and streamline employee preventative health as well as onsite consulting services to help with compliance of Healthcare Entities.

We are seeking a Website Design for Brightpath Rovers, PLLC. Our company’s mission is to provide mobile health and wellness services to employers onsite at their businesses. These services include mobile vaccinations clinics for employees as well as wellness and health screenings. The company will also offer healtcare compliance consulting services for Healthcare Entities. The company was founded to bring these important healthcare services to businesses and keep employees healthy. Healthy employees are the cornerstone to a great business and we want to help orginazations achieve their goals of having a healthy productive workforce.

We are looking for a moderin website design that will need to be coded. We have attached our current logo design for reference as well as a brief questionare regarding our business for your information (not necessary to include all information). We would like something SEO friendly and easy to navigate.

Thank you!

Brightpath Rovers, PLLC

Target Market(s)

Small Businesses

Industry/Entity Type

Healthcare

Coding

Coded - Design and coding required

Number of Pages Required

1 page

Requirements
Nice to have
• SEO Friendly, Incorporate Logo

```html
<!DOCTYPE html>
<html lang="en">
<head>
<meta charset="utf-8">
<title>Brightpath Rovers, PLLC – Mobile Vaccine Clinics</title>
<link href="https://fonts.googleapis.com/css2?family=Poppins:ital,wght@0,400;0,500;0,600;0,700;0,800;1,600;1,700;1,800&display=swap" rel="stylesheet">
<style>
:root{
  --navy:#1d2a6e;
  --blue:#1f46b0;
  --purple:#8c2f9e;
  --magenta:#b0369f;
  --ink:#333a4d;
  --muted:#6d7385;
  --light:#f3f4f8;
  --white:#ffffff;
  --grad:linear-gradient(90deg,var(--blue),var(--purple));
}
*{box-sizing:border-box;margin:0;padding:0}
html,body{width:1200px;height:3964px;overflow:hidden}
body{position:relative;font-family:'Poppins',sans-serif;color:var(--ink);background:var(--white)}
.abs{position:absolute}
.btn{position:absolute;display:inline-block;background:var(--grad);color:var(--white);font-weight:700;font-size:13px;letter-spacing:.5px;text-transform:uppercase;padding:11px 28px;border-radius:22px;text-decoration:none;white-space:nowrap}
.placeholder{position:absolute}

/* header + hero */
.hero{position:absolute;left:0;top:0;width:1200px;height:690px}
.hero-bg{left:0;top:0;width:1200px;height:690px;background:linear-gradient(120deg,#dfe2ea 0%,#f2f3f7 45%,#e3e6ee 100%)}
.brand{position:absolute;display:flex;align-items:center;gap:10px;font-weight:700;color:var(--navy);white-space:nowrap}
.brand .dot{width:34px;height:34px;border-radius:50%;background:var(--purple)}
.hero .brand{left:28px;top:16px;font-size:20px}
.nav{position:absolute;left:530px;top:22px;display:flex;gap:20px;font-size:13px;font-weight:500;color:var(--navy);white-space:nowrap}
.nav .active{background:var(--purple);color:var(--white);padding:4px 14px;border-radius:4px;margin-top:-4px}
.top-call{position:absolute;left:1030px;top:14px;display:flex;align-items:center;gap:8px;white-space:nowrap}
.top-call .ic{width:32px;height:32px;border-radius:50%;background:var(--purple);display:flex;align-items:center;justify-content:center}
.top-call small{display:block;font-size:10px;color:var(--muted)}
.top-call b{font-size:16px;color:var(--navy)}
.hero-photo-left{left:0;top:60px;width:330px;height:630px;background:linear-gradient(180deg,#cfd3de,#a9afc2)}
.hero-van{left:680px;top:370px;width:500px;height:300px;background:linear-gradient(135deg,#eef0f5 0%,#c7cbd8 55%,#7d3aa3 100%);border-radius:30px}
.hero-copy{position:absolute;left:390px;top:36px;width:400px;text-align:center}
.hero-copy h1{font-size:40px;line-height:1.12;font-weight:800;color:var(--navy)}
.hero-copy .tag{margin-top:12px;font-size:11px;font-weight:700;font-style:italic;color:var(--purple);white-space:nowrap}
.hero-copy .reserve{margin-top:14px;font-size:17px;line-height:1.35;color:var(--ink)}
.hero .btn{left:523px;top:298px}
.feature{position:absolute;display:flex;flex-direction:column;align-items:center;width:120px;font-size:11px;font-weight:600;color:var(--navy);text-align:center}
.feature .circle{width:56px;height:56px;border-radius:50%;background:var(--purple);display:flex;align-items:center;justify-content:center;margin-bottom:6px}
.side-tab{position:absolute;left:1176px;top:260px;width:24px;height:110px;background:var(--blue);color:var(--white);font-size:11px;font-weight:600;writing-mode:vertical-rl;display:flex;align-items:center;justify-content:center}

/* section headings */
.sec-title{position:absolute;left:0;width:1200px;text-align:center;font-size:40px;font-weight:800;font-style:italic;color:var(--blue)}
.sec-title span{color:var(--purple)}
.sec-sub{position:absolute;left:0;width:1200px;text-align:center;font-size:13px;color:var(--muted)}

/* schedule */
.step{position:absolute;width:280px;text-align:center}
.diamond{position:relative;margin:0 auto;width:150px;height:150px;transform:rotate(45deg);border-radius:14px;overflow:hidden;box-shadow:0 6px 18px rgba(40,40,90,.18)}
.diamond.a{background:linear-gradient(135deg,#d9dbe6,#8b95b8)}
.diamond.b{background:linear-gradient(135deg,#f1f2f6,#7d3aa3)}
.diamond.c{background:linear-gradient(135deg,#cfe0ea,#6e86a8)}
.step .num{width:40px;height:40px;border-radius:50%;background:var(--grad);color:var(--white);font-weight:700;font-size:13px;display:flex;align-items:center;justify-content:center;margin:36px auto 14px}
.step p{font-size:14px;font-weight:700;font-style:italic;color:var(--navy);line-height:1.35}
.step-line{position:absolute;top:1059px;height:2px;background:#d6d9e4}

/* about */
.about-label{left:80px;top:1380px;font-size:13px;font-weight:600;color:var(--purple)}
.about-title{left:80px;top:1400px;font-size:36px;font-weight:800;font-style:italic;color:var(--navy);white-space:nowrap}
.about-sub{left:80px;top:1452px;font-size:13px;font-weight:600;color:var(--purple)}
.about-text{left:80px;top:1494px;width:430px;font-size:12.5px;line-height:1.6;color:var(--muted)}
.about-text p+p{margin-top:10px}
.about .btn{left:80px;top:1650px}
.about-photo{left:600px;top:1370px;width:600px;height:350px;background:linear-gradient(135deg,#c9d6e2 0%,#8fa6bf 50%,#6a7a98 100%)}

/* services band */
.services-band{left:0;top:1780px;width:1200px;height:720px;background:linear-gradient(110deg,#1d3ea6 0%,#3a3aaa 45%,#8c2f9e 100%);clip-path:polygon(0 12%,100% 0,100% 88%,0 100%)}
.services-title{top:1900px;color:var(--white);font-size:40px}
.services-sub{top:1960px;color:#e3e4f5;line-height:1.5}
.card{position:absolute;top:2060px;width:196px;height:200px;border-radius:10px;background:rgba(10,20,70,.35);border:1px solid rgba(255,255,255,.18);text-align:center;color:var(--white);padding:24px 14px 0}
.card .circle{width:54px;height:54px;border-radius:50%;background:rgba(255,255,255,.9);margin:0 auto 14px;display:flex;align-items:center;justify-content:center}
.card h3{font-size:13px;font-weight:700;font-style:italic;line-height:1.3}
.card p{margin-top:8px;font-size:11px;line-height:1.45;opacity:.85}
.card.featured{top:2030px;height:260px;background:var(--white);color:var(--navy);box-shadow:0 14px 30px rgba(0,0,0,.25)}
.card.featured p{color:var(--muted);opacity:1}
.card.featured .circle{background:var(--light)}
.card.featured .btn{position:static;display:inline-block;margin-top:14px;padding:9px 20px;font-size:11px}

/* recommendations */
.rec-title{top:2540px;font-size:38px}
.rec-sub{top:2594px}
.agency-badge{left:420px;top:2640px;width:140px;height:140px;border-radius:50%;background:var(--white);border:8px solid #c8d3ea;box-shadow:0 4px 14px rgba(0,0,0,.12)}
.rec-van{left:360px;top:2700px;width:520px;height:300px;background:linear-gradient(135deg,#f1f2f6 0%,#c9cdd9 55%,#7d3aa3 100%);border-radius:30px}

/* signup */
.signup-text{left:200px;top:3080px;width:400px;font-size:12.5px;line-height:1.6;color:var(--muted)}
.signup-text p+p{margin-top:10px}
.field{position:absolute;left:630px;width:410px;height:36px;border:1px solid #c9ccd8;border-radius:18px;font-size:12px;color:#9a9fae;padding:9px 18px}
.signup .btn{left:630px;top:3172px;padding:9px 22px}

/* question */
.question-photo{left:170px;top:3300px;width:330px;height:260px;background:linear-gradient(135deg,#e7e9f1 0%,#7a6bb5 60%,#8c2f9e 100%);border-radius:12px}
.q-title{left:560px;top:3350px;font-size:40px;font-weight:800;font-style:italic;color:var(--navy);line-height:1.15;white-space:nowrap}
.q-title span{display:block;color:var(--purple)}
.q-call{position:absolute;left:560px;top:3465px;display:flex;align-items:center;gap:12px}
.q-call .ic{width:44px;height:44px;border-radius:50%;background:var(--purple);display:flex;align-items:center;justify-content:center}
.q-call small{display:block;font-size:12px;color:var(--muted)}
.q-call b{font-size:24px;color:var(--navy)}

/* footer */
.footer{left:0;top:3580px;width:1200px;height:384px;background:linear-gradient(100deg,#1d3ea6 0%,#3b3aaa 50%,#8c2f9e 100%);clip-path:polygon(0 16%,100% 0,100% 100%,0 100%)}
.footer .brand{left:90px;top:110px;color:var(--white);font-size:20px}
.footer .brand .dot{background:var(--white)}
.social{position:absolute;left:110px;top:170px;display:flex;gap:10px}
.social i{width:30px;height:30px;border-radius:50%;background:var(--white);display:block}
.fcol{position:absolute;top:100px;color:var(--white)}
.fcol h4{font-size:17px;font-weight:700;font-style:italic;margin-bottom:12px}
.fcol ul{list-style:none;font-size:12px;line-height:1.9;opacity:.9}
.fcol li::before{content:"›";margin-right:8px}
.contact li{display:flex;gap:10px;align-items:flex-start}
.contact li::before{content:none}
.contact .pin{width:18px;height:18px;border-radius:50%;background:rgba(255,255,255,.25);flex:none;margin-top:2px}
.copyright{position:absolute;left:0;top:355px;width:1200px;text-align:center;font-size:11px;color:#dcdcf0}
</style>
</head>
<body>

<section class="hero">
  <div class="placeholder hero-bg" role="img" aria-label="Bright modern office building facade"></div>
  <div class="placeholder hero-photo-left" role="img" aria-label="Smiling woman holding a phone"></div>
  <div class="brand"><span class="dot"></span>Brightpath Rovers</div>
  <nav class="nav">
    <span class="active">Home</span><span>About</span><span>Services ▾</span><span>Schedule</span><span>Pricing</span><span>Contact</span>
  </nav>
  <div class="top-call">
    <span class="ic"><svg width="16" height="16" viewBox="0 0 24 24"><path fill="#fff" d="M6.6 10.8a15 15 0 0 0 6.6 6.6l2.2-2.2a1 1 0 0 1 1-.25 11.4 11.4 0 0 0 3.6.57 1 1 0 0 1 1 1V20a1 1 0 0 1-1 1A17 17 0 0 1 3 4a1 1 0 0 1 1-1h3.5a1 1 0 0 1 1 1c0 1.25.2 2.45.57 3.57a1 1 0 0 1-.25 1z"/></svg></span>
    <div><small>Call Us</small><b>555-014-2290</b></div>
  </div>
  <div class="hero-copy">
    <h1>Making The Workplace A Healthier Place</h1>
    <p class="tag">No Crowded Waiting Rooms, no long lines, No Hassle!</p>
    <p class="reserve">Reserve Your on-site Mobile<br>Vaccine Clinic Today!</p>
  </div>
  <a class="btn">Schedule Now</a>
  <div class="placeholder hero-van" role="img" aria-label="Branded mobile clinic van"></div>
  <div class="feature" style="left:870px;top:190px"><span class="circle"><svg width="24" height="24" viewBox="0 0 24 24"><path fill="none" stroke="#fff" stroke-width="2.4" d="M5 12l5 5 9-10"/></svg></span>On-Site Mobile Vaccines</div>
  <div class="feature" style="left:730px;top:265px"><span class="circle"><svg width="24" height="24" viewBox="0 0 24 24"><path fill="#fff" d="M12 21s-8-5.3-8-11a4.5 4.5 0 0 1 8-2.8A4.5 4.5 0 0 1 20 10c0 5.7-8 11-8 11z"/></svg></span>Vaccines</div>
  <div class="feature" style="left:935px;top:285px"><span class="circle"><svg width="24" height="24" viewBox="0 0 24 24"><path fill="none" stroke="#fff" stroke-width="2.4" d="M12 5v14M5 12h14"/></svg></span>Hassle Free</div>
  <div class="side-tab">Vaccine Clinic</div>
</section>

<section class="schedule">
  <h2 class="sec-title" style="top:750px">Schedule Today</h2>
  <p class="sec-sub" style="top:808px;font-weight:600;color:var(--navy)">Hassle Free streamlining the vaccination process…</p>
  <p class="sec-sub" style="top:830px">Submit the simple Vaccine Clinic Needs Questionnaire and we will be in touch.</p>
  <div class="step-line" style="left:340px;width:180px"></div>
  <div class="step-line" style="left:680px;width:180px"></div>
  <div class="step" style="left:60px;top:890px">
    <div class="diamond a" role="img" aria-label="Office manager at a laptop"></div>
    <div class="num">01</div>
    <p>Submit Vaccine Clinic Needs Questionnaire.</p>
  </div>
  <div class="step" style="left:460px;top:890px">
    <div class="diamond b" role="img" aria-label="Mobile clinic van"></div>
    <div class="num">02</div>
    <p>Brightpath Rovers, PLLC will Contact you to Schedule on-site Vaccine Clinic.</p>
  </div>
  <div class="step" style="left:860px;top:890px">
    <div class="diamond c" role="img" aria-label="Nurse preparing a vaccine"></div>
    <div class="num">03</div>
    <p>Prepare Your Employees For Vaccine Clinic Day.</p>
  </div>
  <a class="btn" style="left:535px;top:1200px">Schedule Now</a>
</section>

<section class="about">
  <p class="abs about-label">About Us</p>
  <h2 class="abs about-title">Brightpath Rovers, PLLC</h2>
  <p class="abs about-sub">Making the workplace a healthier place</p>
  <div class="abs about-text">
    <p>To provide on-site wellness services to employers that simplify and streamline employee preventative health.</p>
    <p>Brightpath Rovers, PLLC was started by local Washington state licensed pharmacists with over 15 years experience in vaccinating patients. We are highly skilled immunizers.</p>
  </div>
  <a class="btn">Schedule Now</a>
  <div class="placeholder about-photo" role="img" aria-label="Gloved hand giving a vaccine in the upper arm"></div>
</section>

<section class="services">
  <div class="placeholder services-band"></div>
  <h2 class="sec-title services-title">Services We Provide</h2>
  <p class="sec-sub services-sub">Brightpath Rovers will come to you!<br>No crowded waiting rooms, no long lines, no hassle!</p>
  <div class="card" style="left:75px"><span class="circle"><svg width="24" height="24" viewBox="0 0 24 24"><path fill="none" stroke="#8c2f9e" stroke-width="2.4" d="M5 12l5 5 9-10"/></svg></span><h3>Mobile Vaccine Clinics Providing Flu</h3><p>No crowded waiting rooms, no long lines, no hassle!</p></div>
  <div class="card" style="left:290px"><span class="circle"><svg width="24" height="24" viewBox="0 0 24 24"><path fill="none" stroke="#8c2f9e" stroke-width="2.4" d="M12 5v14M5 12h14"/></svg></span><h3>Covid Booster</h3><p>No crowded waiting rooms, no long lines, no hassle!</p></div>
  <div class="card featured" style="left:502px"><span class="circle"><svg width="24" height="24" viewBox="0 0 24 24"><path fill="none" stroke="#8c2f9e" stroke-width="2.4" d="M5 12l5 5 9-10"/></svg></span><h3>Pneumonia Vaccines</h3><p>No crowded waiting rooms, no long lines, no hassle!</p><a class="btn">Schedule Now</a></div>
  <div class="card" style="left:715px"><span class="circle"><svg width="24" height="24" viewBox="0 0 24 24"><path fill="#8c2f9e" d="M12 21s-8-5.3-8-11a4.5 4.5 0 0 1 8-2.8A4.5 4.5 0 0 1 20 10c0 5.7-8 11-8 11z"/></svg></span><h3>Wellness Screenings</h3><p>No crowded waiting rooms, no long lines, no hassle!</p></div>
  <div class="card" style="left:930px"><span class="circle"><svg width="24" height="24" viewBox="0 0 24 24"><path fill="none" stroke="#8c2f9e" stroke-width="2.4" d="M5 12l5 5 9-10"/></svg></span><h3>Consulting Services For WA Healthcare Entities</h3><p>No crowded waiting rooms, no long lines, no hassle!</p></div>
</section>

<section class="recommend">
  <h2 class="sec-title rec-title">NHA Flu Shot <span>Recommendations</span></h2>
  <p class="sec-sub rec-sub">Yearly flu shot between Aug - Dec?</p>
  <div class="placeholder rec-van" role="img" aria-label="Mobile clinic van with workplace health message"></div>
  <div class="placeholder agency-badge" role="img" aria-label="Health agency badge"></div>
</section>

<section class="signup">
  <div class="abs signup-text">
    <p>Book the entire day so employees can get vaccinated on their workplace premises.</p>
    <p>Employees will avoid congested waiting rooms at medical offices and long lines at local pharmacies.</p>
  </div>
  <div class="field" style="top:3076px">Your Name *</div>
  <div class="field" style="top:3124px">Your Email *</div>
  <a class="btn">Signup</a>
</section>

<section class="question">
  <div class="placeholder question-photo" role="img" aria-label="Man with laptop beside large syringes"></div>
  <h2 class="abs q-title">Have Any Question?<span>For More Information !</span></h2>
  <div class="q-call">
    <span class="ic"><svg width="20" height="20" viewBox="0 0 24 24"><path fill="#fff" d="M6.6 10.8a15 15 0 0 0 6.6 6.6l2.2-2.2a1 1 0 0 1 1-.25 11.4 11.4 0 0 0 3.6.57 1 1 0 0 1 1 1V20a1 1 0 0 1-1 1A17 17 0 0 1 3 4a1 1 0 0 1 1-1h3.5a1 1 0 0 1 1 1c0 1.25.2 2.45.57 3.57a1 1 0 0 1-.25 1z"/></svg></span>
    <div><small>Call Us</small><b>555-014-2290</b></div>
  </div>
</section>

<footer class="abs footer">
  <div class="brand"><span class="dot"></span>Brightpath Rovers</div>
  <div class="social"><i></i><i></i><i></i></div>
  <div class="fcol" style="left:410px">
    <h4>Sitemap</h4>
    <ul><li>Home</li><li>About</li><li>Services</li><li>Schedule</li><li>Pricing</li><li>Contact</li></ul>
  </div>
  <div class="fcol" style="left:620px">
    <h4>Services</h4>
    <ul><li>Mobile Vaccine Clinics Providing Flu</li><li>Covid Booster</li><li>Pneumonia Vaccines</li><li>Wellness Screenings</li><li>Consulting Services</li></ul>
  </div>
  <div class="fcol contact" style="left:900px">
    <h4>Contact Us</h4>
    <ul>
      <li><span class="pin"></span><span>Brightpath Rovers, PLLC<br>210 Harbor Lane, Olympia WA</span></li>
      <li><span class="pin"></span><span>555-014-2290</span></li>
      <li><span class="pin"></span><span>hello@brightpathrovers.com</span></li>
    </ul>
  </div>
  <p class="copyright">©Brightpath Rovers, PLLC - 2020. All rights reserved.</p>
</footer>

</body>
</html>
```